for an application under development,
this application will be used for the management of files in a company for several remote collaborators.
it is like an internal messaging system where files will be opened for such and such a person or group of people.

Target Market(s)

business

Number of Pages Required

5+ page

Requirements
Nice to have
• a visual with the view of a connection between computer and / or smart phones
the name of my application; "DulaMStarwick"

```html
<!DOCTYPE html>
<html lang="en">
<head>
<meta charset="utf-8">
<title>DulaMStarwick – Landing Page</title>
<link rel="stylesheet" href="https://fonts.googleapis.com/css2?family=Bebas+Neue&family=Montserrat:wght@300;400;600;700&family=Raleway:wght@300&display=swap">
<style>
  :root {
    --backdrop: #ececec;
    --page: #fbfbfb;
    --ink: #2b2b2b;
    --ink-soft: #3d3d3d;
    --teal: #1fa9bd;
    --mint: #4fe0cc;
    --lime: #b6e68f;
    --dots: #cfcfcf;
    --rule: #8a8a8a;
  }
  * { margin: 0; padding: 0; box-sizing: border-box; }
  html, body { width: 1200px; height: 1200px; overflow: hidden; }
  body { background: var(--backdrop); position: relative; font-family: "Montserrat", sans-serif; }

  .page {
    position: absolute; left: 0; top: 225px;
    width: 1200px; height: 750px;
    background: linear-gradient(180deg, #ffffff 0%, var(--page) 60%, #f2f2f2 100%);
    overflow: hidden;
  }

  .logo-text {
    position: absolute; left: 78px; top: 52px;
    font-family: "Bebas Neue", sans-serif; font-size: 36px;
    letter-spacing: 7px; color: var(--ink);
  }

  .main-nav {
    position: absolute; left: 522px; top: 56px;
    display: flex; gap: 34px;
    font-weight: 300; font-size: 20px; letter-spacing: 2px; color: var(--ink-soft);
  }

  .search-icon { position: absolute; left: 900px; top: 60px; }

  .btn {
    position: absolute; height: 22px; border-radius: 11px;
    color: #fff; font-size: 9.5px; font-weight: 600;
    display: flex; align-items: center; justify-content: center;
    box-shadow: 1px 2px 3px rgba(0,0,0,.18);
  }
  .btn-signin { left: 944px; top: 60px; width: 83px; background: var(--lime); }
  .btn-register { left: 1038px; top: 60px; width: 83px; background: var(--teal); }

  .network-illustration {
    position: absolute; left: 72px; top: 162px; width: 483px; height: 378px;
    border-radius: 50%;
    background: radial-gradient(ellipse at center, #dff6f5 0%, #b9ecea 45%, rgba(79,224,204,.35) 70%, rgba(255,255,255,0) 72%);
  }

  .decor { position: absolute; left: 0; top: 0; }

  .brand-name {
    position: absolute; right: 114px; top: 311px;
    font-family: "Bebas Neue", sans-serif; font-size: 40px;
    letter-spacing: 5px; color: var(--ink);
  }

  .tagline {
    position: absolute; right: 114px; top: 365px; text-align: right;
    font-size: 22px; font-weight: 400; letter-spacing: 2px;
    line-height: 29px; color: var(--ink-soft);
  }

  .description {
    position: absolute; right: 114px; top: 437px; text-align: right;
    font-family: "Raleway", sans-serif; font-weight: 300;
    font-size: 14px; line-height: 18.7px; color: var(--ink-soft);
  }

  .btn-download {
    position: absolute; left: 795px; top: 532px; width: 178px; height: 35px;
    border-radius: 18px; background: var(--lime); color: #fff;
    font-size: 14px; font-weight: 600;
    display: flex; align-items: center; justify-content: center;
    box-shadow: 1px 3px 4px rgba(0,0,0,.18);
  }
</style>
</head>
<body>
  <main class="page">
    <div class="logo-text">Your Logo Here</div>

    <nav class="main-nav">
      <span>home</span><span>shop</span><span>info</span><span>about us</span>
    </nav>

    <svg class="search-icon" width="18" height="18" viewBox="0 0 18 18" aria-label="search">
      <circle cx="7" cy="7" r="5" fill="none" stroke="#2b2b2b" stroke-width="2"/>
      <line x1="10.8" y1="10.8" x2="16" y2="16" stroke="#2b2b2b" stroke-width="2.4" stroke-linecap="round"/>
    </svg>

    <div class="btn btn-signin">sign in</div>
    <div class="btn btn-register">registration</div>

    <div class="network-illustration" role="img" aria-label="Isometric illustration of a desktop computer, laptop and smartphone linked by a network of communication icons"></div>

    <svg class="decor" width="1200" height="750" viewBox="0 0 1200 750">
      <g stroke="var(--dots)" stroke-width="1.4" stroke-dasharray="1.4 3.6" stroke-linecap="round">
        <line x1="983" y1="148" x2="1193" y2="148"/>
        <line x1="1000" y1="165" x2="1193" y2="165"/>
        <line x1="1008" y1="182" x2="1193" y2="182"/>
        <line x1="1015" y1="200" x2="1193" y2="200"/>
        <line x1="1023" y1="217" x2="1193" y2="217"/>
        <line x1="1030" y1="235" x2="1193" y2="235"/>
        <line x1="1043" y1="252" x2="1193" y2="252"/>
        <line x1="1060" y1="270" x2="1193" y2="270"/>
        <line x1="2" y1="549" x2="130" y2="549"/>
        <line x1="2" y1="566" x2="138" y2="566"/>
        <line x1="2" y1="584" x2="146" y2="584"/>
        <line x1="2" y1="601" x2="154" y2="601"/>
        <line x1="2" y1="619" x2="163" y2="619"/>
        <line x1="2" y1="636" x2="172" y2="636"/>
        <line x1="2" y1="654" x2="182" y2="654"/>
        <line x1="2" y1="671" x2="193" y2="671"/>
      </g>
      <g fill="none" stroke="var(--rule)" stroke-width="1" stroke-dasharray="1 3">
        <polyline points="839,334 708,334 708,459 531,459"/>
        <polyline points="588,459 588,554 781,554"/>
      </g>
      <circle cx="839" cy="334" r="2.2" fill="var(--rule)"/>
      <circle cx="781" cy="554" r="2.2" fill="var(--rule)"/>
      <g fill="none" stroke="#333" stroke-width="1.1">
        <circle cx="525" cy="186" r="6.5"/>
        <circle cx="116" cy="510" r="6.5"/>
        <circle cx="481" cy="516" r="6.5"/>
        <path d="M536 169h9M540.5 164.5v9M578 185h9M582.5 180.5v9M129 492h9M133.5 487.5v9M86 553h9M90.5 548.5v9M457 529h9M461.5 524.5v9M511 554h9M515.5 549.5v9"/>
      </g>
      <g fill="#333">
        <circle cx="504" cy="159" r="1.2"/><circle cx="548" cy="186" r="1.2"/>
        <circle cx="537" cy="224" r="1.2"/><circle cx="157" cy="503" r="1.2"/>
        <circle cx="128" cy="548" r="1.2"/><circle cx="117" cy="582" r="1.2"/>
        <circle cx="494" cy="524" r="1.2"/><circle cx="471" cy="569" r="1.2"/>
      </g>
    </svg>

    <h1 class="brand-name">DulaMStarwick</h1>
    <p class="tagline">YOUR INTERNAL<br>MESSAGING NETWORK</p>
    <p class="description">
      This application will be used for the management of<br>
      files in a company for several remote collaborators.<br>
      it is like an internal messaging system where files will be<br>
      opened for such and such a person or group of people.
    </p>
    <div class="btn-download">DOWNLOAD APP</div>
  </main>
</body>
</html>
```